One page wordpress horizontal and/or vertical website.

I attached my company logo and a rough draft outline of the one page website. Include a call to action button were appropriate. I have provided 4 brand logo examples (see the attached outline). Please provide the hero shot.

About Us

Target Market(s)

This is technology company that targeting investors to raise capital

Industry/Entity Type

Technology

Coding

Coded - Design and coding required

Font styles to use
Sans Serif
Other font styles liked:
• Add script font if needed.

Requirements
Must have
• at least 2 of the proofs to have horizontal sliders
Nice to have
• A video with a moving red shark fin

```html
<!DOCTYPE html>
<html lang="en">
<head>
<meta charset="utf-8">
<title>Crimson Fin – One Page Website Proofs</title>
<link href="https://fonts.googleapis.com/css2?family=Poppins:wght@400;500;600;700;800&display=swap" rel="stylesheet">
<style>
  :root{
    --stage:#d9d9d9;
    --red:#c8161d;
    --red-dark:#8e0c10;
    --ink:#1d1d1d;
    --text:#555;
    --muted:#9a9a9a;
    --white:#ffffff;
    --line:#e3e3e3;
    --footer:#0d0d0d;
    --sky-top:#ffffff;
    --sky-bottom:#c9d6e2;
  }
  *{box-sizing:border-box;margin:0;padding:0}
  html,body{width:711px;height:1200px;overflow:hidden}
  body{background:var(--stage);font-family:'Poppins',sans-serif;color:var(--ink);position:relative}

  .page{position:absolute;top:16px;width:299px;height:1162px;background:var(--white);display:flex;flex-direction:column;overflow:hidden;box-shadow:0 2px 8px rgba(0,0,0,.15)}
  .page--white-contact{left:28px}
  .page--red-contact{left:384px}

  /* nav */
  .site-nav{height:24px;display:flex;align-items:center;justify-content:space-between;padding:0 14px;position:relative;background:var(--white)}
  .brand-name{font-weight:700;font-size:8px;color:var(--red);display:flex;align-items:center;gap:3px}
  .brand-name .dot{width:5px;height:5px;border-radius:50%;background:var(--red)}
  .menu{display:flex;gap:7px;font-size:3.6px;font-weight:600;color:var(--ink);margin-top:7px}
  .menu .is-active{color:var(--red)}
  .nav-cta{position:absolute;right:14px;top:3px;background:var(--red);color:var(--white);font-size:3.4px;font-weight:600;padding:1.5px 6px;border-radius:2px}

  /* hero */
  .hero{height:196px;position:relative}
  .hero-photo{position:absolute;inset:0;background:linear-gradient(100deg,#6b6b6b 0%,#9a9a9a 45%,#8c2a2c 70%,#c8161d 85%,#7d7d7d 100%)}
  .hero-copy{position:absolute;left:18px;top:42px;color:var(--white)}
  .hero-copy .eyebrow{font-size:11px;font-weight:700;letter-spacing:.2px}
  .hero-copy h1{font-size:23px;font-weight:800;line-height:1.05}
  .hero-copy .hero-btn{display:inline-block;margin-top:6px;font-size:3.6px;background:var(--red);padding:2px 7px;border-radius:2px;font-weight:600}
  .hero-wave{position:absolute;left:0;bottom:-1px;width:100%;height:40px}

  /* about */
  .about{height:190px;position:relative;padding:30px 16px 0}
  .ghost{position:absolute;left:0;right:0;text-align:center;font-weight:800;color:#f1f1f1;letter-spacing:1px;font-size:34px;line-height:1}
  .about .ghost{top:0}
  .about-row{position:relative;display:flex;gap:12px}
  .about-media{position:relative;width:98px;height:96px;flex:none}
  .about-accent{position:absolute;left:-5px;bottom:-5px;width:40px;height:60px;background:var(--red)}
  .about-photo{position:absolute;inset:0;background:linear-gradient(180deg,#8fb8df 0%,#4b84bd 55%,#1f4f86 100%)}
  .play{position:absolute;right:-8px;bottom:8px;width:16px;height:16px;border-radius:50%;background:var(--red);display:flex;align-items:center;justify-content:center}
  .about-text h2{font-size:10px;font-weight:700;margin:4px 0 5px}
  .about-text p{font-size:4.4px;line-height:1.55;color:var(--text);margin-bottom:4px}

  /* brands */
  .brands{height:430px;position:relative;background:linear-gradient(180deg,var(--sky-top) 0%,var(--sky-top) 35%,var(--sky-bottom) 100%);padding:22px 12px 0}
  .brands .ghost{top:10px}
  .brands h2{position:relative;text-align:center;font-size:11.5px;font-weight:700;margin-bottom:16px}
  .brand-card{position:relative;height:71px;background:var(--white);border-radius:9px;box-shadow:0 2px 6px rgba(0,0,0,.12);margin-bottom:14px;display:flex;align-items:center;padding:0 10px;gap:10px}
  .brand-logo{width:52px;height:28px;flex:none;display:flex;align-items:center;justify-content:center;font-size:8px;font-weight:700;color:var(--ink)}
  .brand-info{flex:1}
  .brand-info h3{font-size:6px;color:var(--red);font-weight:700;margin-bottom:3px}
  .brand-info p{font-size:3.8px;line-height:1.55;color:var(--text)}
  .brand-badge{width:42px;height:42px;border-radius:50%;background:#f2f2f2;flex:none;display:flex;align-items:center;justify-content:center;font-size:7px;font-weight:700;color:#3a3a8a}

  /* contact */
  .contact{height:208px;position:relative;padding:22px 26px 0;text-align:center}
  .contact .ghost{top:8px}
  .contact h2{position:relative;font-size:11px;font-weight:700}
  .contact .lede{position:relative;font-size:4.2px;line-height:1.5;color:var(--text);margin:3px 16px 10px}
  .contact-form{position:relative;display:grid;grid-template-columns:1fr 1fr;gap:6px 8px;text-align:left}
  .field{font-size:3.6px;color:var(--muted)}
  .field span{display:block;margin-bottom:1.5px}
  .field i{display:block;height:9px;background:var(--white);border:.6px solid var(--line)}
  .field--message{grid-column:1 / -1}
  .field--message i{height:34px}
  .submit{grid-column:1 / -1;justify-self:center;background:var(--red);color:var(--white);font-size:3.8px;font-weight:600;padding:2.5px 12px;border-radius:6px;margin-top:2px}
  .page--red-contact .contact{background:radial-gradient(ellipse at 50% 40%,#d3242a 0%,var(--red) 45%,var(--red-dark) 100%);color:var(--white)}
  .page--red-contact .contact .ghost{color:rgba(255,255,255,.07)}
  .page--red-contact .contact .lede{color:#f3d0d0}
  .page--red-contact .field{color:#f3d0d0}
  .page--red-contact .field i{border-color:transparent}
  .page--red-contact .submit{background:var(--footer)}

  /* footer */
  .site-footer{flex:1;position:relative;background:var(--footer);color:var(--white);text-align:center}
  .footer-wave{position:absolute;left:0;top:-1px;width:100%;height:30px}
  .footer-brand{position:relative;margin-top:36px;display:flex;justify-content:center}
  .footer-contacts{display:flex;justify-content:center;gap:30px;margin-top:14px;font-size:3.6px;color:#cfcfcf}
  .footer-contacts div{display:flex;align-items:center;gap:3px;text-align:left}
  .footer-contacts svg{width:9px;height:9px}
  .copyright{position:absolute;left:0;right:0;bottom:6px;font-size:3.2px;color:#888}
</style>
</head>
<body>

<!-- Proof A -->
<article class="page page--white-contact">
  <nav class="site-nav">
    <div class="brand-name"><span class="dot"></span>Crimson Fin</div>
    <ul class="menu" style="list-style:none"><li class="is-active">HOME</li><li>ABOUT US</li><li>PARTNERS</li><li>CONTACT US</li></ul>
    <span class="nav-cta">INVEST NOW</span>
  </nav>

  <header class="hero">
    <div class="hero-photo" role="img" aria-label="Hero video still: red shark fin cutting through dark grey water"></div>
    <div class="hero-copy">
      <p class="eyebrow">FIND THE NEXT</p>
      <h1>BIG THING</h1>
      <span class="hero-btn">INVEST NOW</span>
    </div>
    <svg class="hero-wave" viewBox="0 0 299 40" preserveAspectRatio="none">
      <path d="M0 22 C70 4 150 38 299 10 L299 40 L0 40Z" fill="#c8161d"/>
      <path d="M0 28 C80 12 160 42 299 18 L299 40 L0 40Z" fill="#ffffff"/>
    </svg>
  </header>

  <section class="about">
    <div class="ghost">ABOUT US</div>
    <div class="about-row">
      <div class="about-media">
        <div class="about-accent"></div>
        <div class="about-photo" role="img" aria-label="Photo of a red shark fin in blue ocean water"></div>
        <div class="play"><svg width="6" height="6" viewBox="0 0 6 6"><path d="M1 0.5 L5.5 3 L1 5.5Z" fill="#fff"/></svg></div>
      </div>
      <div class="about-text">
        <h2>About Us</h2>
        <p>We scout early technology ventures with bold ideas and strong teams, then help them grow into market leaders through capital and guidance.</p>
        <p>Our investors gain early access to vetted brands, clear reporting and a partner who moves fast when the right chance appears.</p>
      </div>
    </div>
  </section>

  <section class="brands">
    <div class="ghost">BRANDS</div>
    <h2>Development stage brands</h2>
    <div class="brand-card">
      <div class="brand-logo">Nova</div>
      <div class="brand-info"><h3>Nova Brand</h3><p>Smart tools that help small teams plan, share and launch work faster every day.</p></div>
      <div class="brand-badge"></div>
    </div>
    <div class="brand-card">
      <div class="brand-info"><h3>Kelp Brand</h3><p>A simple platform connecting local makers with buyers across new online markets.</p></div>
      <div class="brand-badge">Kelp</div>
    </div>
    <div class="brand-card">
      <div class="brand-logo">Tidal</div>
      <div class="brand-info"><h3>Tidal Brand</h3><p>Clear finance software that keeps records, taxes and reports in one calm place.</p></div>
      <div class="brand-badge"></div>
    </div>
    <div class="brand-card">
      <div class="brand-info"><h3>Reef Brand</h3><p>Cloud storage built for creative teams who need speed, safety and easy sharing.</p></div>
      <div class="brand-badge">Reef</div>
    </div>
  </section>

  <section class="contact">
    <div class="ghost">CONTACT</div>
    <h2>Contact Us</h2>
    <p class="lede">Ready to back the next big idea? Send us a note and our team will reply soon.</p>
    <form class="contact-form">
      <label class="field"><span>Name</span><i></i></label>
      <label class="field"><span>Email</span><i></i></label>
      <label class="field"><span>Phone</span><i></i></label>
      <label class="field"><span>Subject</span><i></i></label>
      <label class="field field--message"><span>Message</span><i></i></label>
      <span class="submit">SUBMIT</span>
    </form>
  </section>

  <footer class="site-footer">
    <svg class="footer-wave" viewBox="0 0 299 30" preserveAspectRatio="none">
      <path d="M0 0 L299 0 L299 8 C200 30 110 -2 0 20Z" fill="#ffffff"/>
      <path d="M0 20 C110 -2 200 30 299 8 L299 14 C200 34 110 6 0 26Z" fill="#c8161d"/>
    </svg>
    <div class="footer-brand"><div class="brand-name"><span class="dot"></span>Crimson Fin</div></div>
    <div class="footer-contacts">
      <div><svg viewBox="0 0 10 10"><circle cx="5" cy="5" r="5" fill="#c8161d"/><path d="M3.2 2.8 L4.2 2.6 L4.6 4 L4 4.5 C4.4 5.3 4.9 5.8 5.6 6.1 L6.1 5.5 L7.4 6 L7.2 7 C5.2 7.2 3 5 3.2 2.8Z" fill="#fff"/></svg><span>Call us<br>(000) 555-0147</span></div>
      <div><svg viewBox="0 0 10 10"><circle cx="5" cy="5" r="5" fill="#c8161d"/><path d="M5 2.2 C6.3 2.2 7 3.1 7 4.1 C7 5.4 5 7.8 5 7.8 C5 7.8 3 5.4 3 4.1 C3 3.1 3.7 2.2 5 2.2Z" fill="#fff"/><circle cx="5" cy="4.1" r=".8" fill="#c8161d"/></svg><span>Visit us<br>12 Harbor Lane</span></div>
    </div>
    <p class="copyright">© 2024 Crimson Fin. All rights reserved.</p>
  </footer>
</article>

<!-- Proof B -->
<article class="page page--red-contact">
  <nav class="site-nav">
    <div class="brand-name"><span class="dot"></span>Crimson Fin</div>
    <ul class="menu" style="list-style:none"><li class="is-active">HOME</li><li>ABOUT US</li><li>PARTNERS</li><li>CONTACT US</li></ul>
    <span class="nav-cta">INVEST NOW</span>
  </nav>

  <header class="hero">
    <div class="hero-photo" role="img" aria-label="Hero video still: red shark fin cutting through dark grey water"></div>
    <div class="hero-copy">
      <p class="eyebrow">FIND THE NEXT</p>
      <h1>BIG THING</h1>
      <span class="hero-btn">INVEST NOW</span>
    </div>
    <svg class="hero-wave" viewBox="0 0 299 40" preserveAspectRatio="none">
      <path d="M0 22 C70 4 150 38 299 10 L299 40 L0 40Z" fill="#c8161d"/>
      <path d="M0 28 C80 12 160 42 299 18 L299 40 L0 40Z" fill="#ffffff"/>
    </svg>
  </header>

  <section class="about">
    <div class="ghost">ABOUT US</div>
    <div class="about-row">
      <div class="about-media">
        <div class="about-accent"></div>
        <div class="about-photo" role="img" aria-label="Photo of a red shark fin in blue ocean water"></div>
        <div class="play"><svg width="6" height="6" viewBox="0 0 6 6"><path d="M1 0.5 L5.5 3 L1 5.5Z" fill="#fff"/></svg></div>
      </div>
      <div class="about-text">
        <h2>About Us</h2>
        <p>We scout early technology ventures with bold ideas and strong teams, then help them grow into market leaders through capital and guidance.</p>
        <p>Our investors gain early access to vetted brands, clear reporting and a partner who moves fast when the right chance appears.</p>
      </div>
    </div>
  </section>

  <section class="brands">
    <div class="ghost">BRANDS</div>
    <h2>Development stage brands</h2>
    <div class="brand-card">
      <div class="brand-logo">Nova</div>
      <div class="brand-info"><h3>Nova Brand</h3><p>Smart tools that help small teams plan, share and launch work faster every day.</p></div>
      <div class="brand-badge"></div>
    </div>
    <div class="brand-card">
      <div class="brand-info"><h3>Kelp Brand</h3><p>A simple platform connecting local makers with buyers across new online markets.</p></div>
      <div class="brand-badge">Kelp</div>
    </div>
    <div class="brand-card">
      <div class="brand-logo">Tidal</div>
      <div class="brand-info"><h3>Tidal Brand</h3><p>Clear finance software that keeps records, taxes and reports in one calm place.</p></div>
      <div class="brand-badge"></div>
    </div>
    <div class="brand-card">
      <div class="brand-info"><h3>Reef Brand</h3><p>Cloud storage built for creative teams who need speed, safety and easy sharing.</p></div>
      <div class="brand-badge">Reef</div>
    </div>
  </section>

  <section class="contact">
    <div class="ghost">CONTACT</div>
    <h2>Contact Us</h2>
    <p class="lede">Ready to back the next big idea? Send us a note and our team will reply soon.</p>
    <form class="contact-form">
      <label class="field"><span>Name</span><i></i></label>
      <label class="field"><span>Email</span><i></i></label>
      <label class="field"><span>Phone</span><i></i></label>
      <label class="field"><span>Subject</span><i></i></label>
      <label class="field field--message"><span>Message</span><i></i></label>
      <span class="submit">SUBMIT</span>
    </form>
  </section>

  <footer class="site-footer">
    <svg class="footer-wave" viewBox="0 0 299 30" preserveAspectRatio="none">
      <path d="M0 0 L299 0 L299 8 C200 30 110 -2 0 20Z" fill="#a5121a"/>
      <path d="M0 20 C110 -2 200 30 299 8 L299 14 C200 34 110 6 0 26Z" fill="#c8161d"/>
    </svg>
    <div class="footer-brand"><div class="brand-name"><span class="dot"></span>Crimson Fin</div></div>
    <div class="footer-contacts">
      <div><svg viewBox="0 0 10 10"><circle cx="5" cy="5" r="5" fill="#c8161d"/><path d="M3.2 2.8 L4.2 2.6 L4.6 4 L4 4.5 C4.4 5.3 4.9 5.8 5.6 6.1 L6.1 5.5 L7.4 6 L7.2 7 C5.2 7.2 3 5 3.2 2.8Z" fill="#fff"/></svg><span>Call us<br>(000) 555-0147</span></div>
      <div><svg viewBox="0 0 10 10"><circle cx="5" cy="5" r="5" fill="#c8161d"/><path d="M5 2.2 C6.3 2.2 7 3.1 7 4.1 C7 5.4 5 7.8 5 7.8 C5 7.8 3 5.4 3 4.1 C3 3.1 3.7 2.2 5 2.2Z" fill="#fff"/><circle cx="5" cy="4.1" r=".8" fill="#c8161d"/></svg><span>Visit us<br>12 Harbor Lane</span></div>
    </div>
    <p class="copyright">© 2024 Crimson Fin. All rights reserved.</p>
  </footer>
</article>

</body>
</html>
```